PowerPoint Template for Consultancy Company.

We need a Power Point template for a Consultancy company based in Copenhagen, Denmark. We focus on supporting people and small companies in starting up next generation technology companies. Company name is "Vorbek-Halstrup Consulting". The template shall demonstrate growth, agility, next generation technology and following your dreams. Please include the uploaded logo.
Updates
Hi guys,
thanks for helping me on this project.
I like the font "Good Times" that is being used in my logo. I will like this to be used as minimum in the headlines in my power point template. I am not sure if it will work on standard text - but will relay on your judgement.
Kind regards
Torvald
Colors
Designer to choose colors to be used in the design.
Look and feel
Each slider illustrates characteristics of the customer's brand and the style your logo design should communicate.

```html
<!DOCTYPE html>
<html lang="en">
<head>
<meta charset="utf-8">
<title>Vorbek-Halstrup Consulting – Presentation Template</title>
<link href="https://fonts.googleapis.com/css2?family=Michroma&family=Montserrat:wght@400;600;700&display=swap" rel="stylesheet">
<style>
:root{
  --page:#ffffff;
  --sky:#cfe0ef;
  --sky-deep:#b7cde2;
  --navy:#1d2857;
  --ink:#22304f;
  --steel:#3f5f8f;
  --photo-a:#2f5b8e;
  --photo-b:#9fc0dd;
  --grey:#6f7480;
  --violet:#3b3a8f;
  --white:#ffffff;
}
*{box-sizing:border-box;margin:0;padding:0}
html,body{width:1200px;height:2200px;overflow:hidden;background:var(--page)}
body{font-family:"Montserrat",sans-serif;color:var(--ink);position:relative}

/* hero cover slide */
.cover{position:absolute;left:120px;top:20px;width:960px;height:540px;background:var(--sky);overflow:hidden}
.cover-photo{position:absolute;left:0;top:0;width:560px;height:540px;background:linear-gradient(135deg,var(--photo-a),var(--photo-b))}
.cover-shape{position:absolute;left:0;top:0}
.cover-brand{position:absolute;left:575px;top:235px;width:375px;text-align:center;font-family:"Michroma",sans-serif;color:var(--navy);white-space:nowrap}
.cover-brand .name{font-size:21px;letter-spacing:.5px;line-height:1.35}
.cover-brand .sub{font-size:19px;letter-spacing:5px;margin-top:6px}

/* feature list */
.features{position:absolute;left:60px;top:590px;width:1080px;display:grid;grid-template-columns:1fr 1fr;gap:40px;font-weight:700;font-size:19px;color:var(--ink)}
.features li{list-style:none;display:flex;gap:10px;line-height:1.35;margin-bottom:4px}
.box{flex:none;width:15px;height:15px;border:2px solid var(--ink);margin-top:4px}
.features .sub{padding-left:25px;font-weight:700}

/* slide deck */
.deck{position:absolute;left:60px;top:860px;display:grid;grid-template-columns:repeat(3,340px);grid-auto-rows:177px;gap:14px 30px}
.slide{position:relative;background:var(--sky);overflow:hidden}
.slide > *{position:absolute}
.h{font-family:"Michroma",sans-serif;color:var(--navy);font-size:11px;letter-spacing:.5px}
.h.lg{font-size:15px}
.h.light{color:var(--white)}
.p{font-size:5.5px;line-height:1.5;color:var(--ink)}
.p.light{color:var(--white)}
.photo{background:linear-gradient(135deg,var(--photo-a),var(--photo-b))}
.photo.dark{background:linear-gradient(135deg,#3c4150,#8a93a3)}
.mini-brand{font-family:"Michroma",sans-serif;color:var(--navy);font-size:6px;letter-spacing:.5px;text-align:center;line-height:1.3}
.rule{height:1px;background:var(--white)}
.circ{width:22px;height:22px;border-radius:50%;background:var(--grey)}
.stat{font-family:"Michroma",sans-serif;color:var(--navy);font-size:12px;white-space:nowrap}
.tile{background:#2f3240}
table{border-collapse:collapse;font-size:5.5px}
td,th{padding:3px 6px;text-align:left}
th{background:var(--violet);color:var(--white);font-weight:600}
td{background:var(--white)}
tr:nth-child(odd) td{background:#e6eef6}
</style>
</head>
<body>

<section class="cover">
  <div class="cover-photo" role="img" aria-label="Photo of a business team working together"></div>
  <svg class="cover-shape" width="560" height="540" viewBox="0 0 560 540">
    <polygon points="0,190 170,360 350,180 560,390 560,540 0,540" fill="#1d2857" opacity=".9"/>
    <polygon points="0,0 560,0 560,120 350,0" fill="#cfe0ef" opacity=".35"/>
  </svg>
  <div class="cover-brand">
    <div class="name">VORBEK-HALSTRUP</div>
    <div class="sub">CONSULTING</div>
  </div>
</section>

<section class="features">
  <ul>
    <li><span class="box"></span>Ratio 16:9</li>
    <li><span class="box"></span>Full HD</li>
    <li><span class="box"></span>Custom color pallet</li>
    <li><span class="box"></span>Custom Font - Easy Change</li>
    <li><span class="box"></span>Easy to edit, just drag and drop images</li>
  </ul>
  <ul>
    <li><span class="box"></span>Can be included up to 100 slides;</li>
    <li class="sub">* Text + images (1,2,3,4) , Text Slides</li>
    <li class="sub">* Portfolio Slides , blog slides</li>
    <li class="sub">* Text Slides, infographics</li>
    <li class="sub">* Data Slides</li>
    <li><span class="box"></span>In the sample you find 19 slides</li>
  </ul>
</section>

<section class="deck">
  <!-- 1 agenda -->
  <article class="slide">
    <div class="h" style="left:14px;top:14px">AGENDA</div>
    <div class="p" style="left:14px;top:40px;width:110px">About us<br>Our services<br>Our team<br>Portfolio<br>Contact</div>
    <div class="rule" style="left:14px;top:90px;width:110px"></div>
    <div class="photo" style="left:150px;top:20px;width:175px;height:137px" role="img" aria-label="Photo of a laptop on a desk"></div>
  </article>
  <!-- 2 services -->
  <article class="slide">
    <div class="h" style="left:14px;top:14px">OUR SERVICES</div>
    <div class="p" style="left:14px;top:40px;width:130px">We help founders and small teams turn bold ideas into next generation technology companies.</div>
    <div class="photo" style="left:170px;top:0;width:170px;height:177px" role="img" aria-label="Photo of a person at a computer screen"></div>
  </article>
  <!-- 3 about -->
  <article class="slide">
    <div class="photo" style="left:0;top:0;width:190px;height:177px" role="img" aria-label="Photo of a modern office screen"></div>
    <div class="mini-brand" style="left:200px;top:20px;width:130px">VORBEK-HALSTRUP<br>CONSULTING</div>
    <div class="p" style="left:210px;top:60px;width:115px">Based in Copenhagen, we support people chasing their dreams with agile growth.</div>
  </article>
  <!-- 4 what we do -->
  <article class="slide">
    <div class="h" style="left:14px;top:14px">WHAT WE DO</div>
    <div class="circ" style="left:30px;top:50px"></div><div class="p" style="left:58px;top:57px">Strategy</div>
    <div class="circ" style="left:190px;top:50px"></div><div class="p" style="left:218px;top:57px">Funding</div>
    <div class="circ" style="left:30px;top:80px"></div><div class="p" style="left:58px;top:87px">Growth</div>
    <div class="circ" style="left:190px;top:80px"></div><div class="p" style="left:218px;top:87px">Technology</div>
    <div class="circ" style="left:30px;top:110px"></div><div class="p" style="left:58px;top:117px">Agility</div>
    <div class="circ" style="left:190px;top:110px"></div><div class="p" style="left:218px;top:117px">Mentoring</div>
    <div class="circ" style="left:30px;top:140px"></div><div class="p" style="left:58px;top:147px">Network</div>
    <div class="circ" style="left:190px;top:140px"></div><div class="p" style="left:218px;top:147px">Launch</div>
  </article>
  <!-- 5 timeline -->
  <article class="slide">
    <div class="h" style="left:14px;top:14px">TIMELINE</div>
    <div class="rule" style="left:14px;top:45px;width:312px"></div>
    <div class="p" style="left:14px;top:55px;width:70px"><b>2021</b><br>Idea and first team formed.</div>
    <div class="p" style="left:94px;top:55px;width:70px"><b>2022</b><br>First prototype tested.</div>
    <div class="p" style="left:174px;top:55px;width:70px"><b>2023</b><br>Seed funding secured.</div>
    <div class="p" style="left:254px;top:55px;width:70px"><b>2024</b><br>Product launched abroad.</div>
  </article>
  <!-- 6 goals -->
  <article class="slide">
    <div class="h lg" style="left:14px;top:40px">OUR GOALS</div>
    <div class="p" style="left:14px;top:70px;width:150px">We guide startups from first idea to a growing business with clear goals.</div>
    <div style="left:200px;top:20px;width:126px;height:137px;background:var(--white)"></div>
    <div class="p" style="left:212px;top:35px;width:105px"><b>01</b> Build vision<br><br><b>02</b> Grow fast<br><br><b>03</b> Scale smart</div>
  </article>
  <!-- 7 founder -->
  <article class="slide">
    <div class="photo dark" style="left:20px;top:40px;width:95px;height:95px;border-radius:50%" role="img" aria-label="Portrait photo of the founder"></div>
    <div class="h" style="left:140px;top:40px">OUR FOUNDER</div>
    <div class="p" style="left:140px;top:60px;width:180px"><b>Torvald</b><br>Founder and lead consultant helping new tech companies grow.</div>
  </article>
  <!-- 8 portfolio -->
  <article class="slide">
    <div class="h" style="left:14px;top:10px">PORTFOLIO</div>
    <div style="left:14px;top:32px;width:312px;height:135px;display:grid;grid-template-columns:repeat(4,1fr);gap:6px" role="img" aria-label="Grid of eight project photos">
      <div class="photo dark"></div><div class="photo dark"></div><div class="photo dark"></div><div class="photo dark"></div>
      <div class="photo dark"></div><div class="photo dark"></div><div class="photo dark"></div><div class="photo dark"></div>
    </div>
  </article>
  <!-- 9 gallery -->
  <article class="slide">
    <div style="left:14px;top:20px;width:312px;height:137px;display:grid;grid-template-columns:repeat(4,1fr);gap:6px" role="img" aria-label="Grid of eight project photos">
      <div class="photo"></div><div class="photo"></div><div class="photo"></div><div class="photo"></div>
      <div class="photo"></div><div class="photo"></div><div class="photo"></div><div class="photo"></div>
    </div>
  </article>
  <!-- 10 tiles -->
  <article class="slide">
    <div style="left:40px;top:30px;width:260px;height:117px;display:grid;grid-template-columns:repeat(5,1fr);gap:8px" role="img" aria-label="Grid of ten image placeholders">
      <div class="tile"></div><div class="tile"></div><div class="tile"></div><div class="tile"></div><div class="tile"></div>
      <div class="tile"></div><div class="tile"></div><div class="tile"></div><div class="tile"></div><div class="tile"></div>
    </div>
  </article>
  <!-- 11 entrepreneurship -->
  <article class="slide" style="background:var(--sky-deep)">
    <div class="h light" style="left:150px;top:22px;width:180px;font-size:10px;line-height:1.45">CREATE A GOOD<br>ENTREPRENEURSHIP</div>
    <div style="left:20px;top:90px;width:140px;height:60px;background:var(--white)"></div>
    <div class="p" style="left:28px;top:98px;width:125px">Start small, test often and let your dream guide every step.</div>
    <div class="p" style="left:180px;top:98px;width:140px"><b>Our approach</b><br>Agile methods for fast learning.</div>
  </article>
  <!-- 12 approach -->
  <article class="slide">
    <div class="h" style="left:170px;top:20px;width:160px;line-height:1.4">SUPPORTING YOUR NEXT STEP</div>
    <div class="p" style="left:170px;top:60px;width:150px">From pitch to product, we stand by your side.</div>
    <div class="p" style="left:170px;top:90px;width:150px">Clear plans, honest advice, real results.</div>
    <div class="photo" style="left:14px;top:20px;width:140px;height:137px" role="img" aria-label="Photo of a team meeting"></div>
  </article>
  <!-- 13 numbers -->
  <article class="slide">
    <div class="h" style="left:14px;top:14px">NUMBERS</div>
    <div class="stat" style="left:20px;top:50px">800</div>
    <div class="stat" style="left:140px;top:50px">97%</div>
    <div class="stat" style="left:250px;top:50px">9%</div>
    <div class="p" style="left:20px;top:70px">Clients</div><div class="p" style="left:140px;top:70px">Success</div><div class="p" style="left:250px;top:70px">Growth</div>
    <div class="stat" style="left:20px;top:110px">$150,000</div>
    <div class="stat" style="left:140px;top:110px">85,000</div>
    <div class="stat" style="left:250px;top:110px">5%</div>
    <div class="p" style="left:20px;top:130px">Funding</div><div class="p" style="left:140px;top:130px">Hours</div><div class="p" style="left:250px;top:130px">Costs</div>
  </article>
  <!-- 14 photo overlay -->
  <article class="slide">
    <div class="photo" style="left:0;top:0;width:340px;height:177px" role="img" aria-label="Photo of a city office building"></div>
    <div style="left:30px;top:40px;width:140px;height:97px;background:var(--navy);opacity:.85"></div>
    <div class="h light" style="left:42px;top:52px">OUR VISION</div>
    <div class="p light" style="left:42px;top:74px;width:118px">Helping the next generation of founders build the future.</div>
  </article>
  <!-- 15 text and photo -->
  <article class="slide">
    <div class="h" style="left:14px;top:20px">OUR STORY</div>
    <div class="p" style="left:14px;top:45px;width:140px">We started in Copenhagen with one idea: every dream deserves a plan.</div>
    <div class="photo" style="left:180px;top:20px;width:146px;height:137px" role="img" aria-label="Photo of a workspace"></div>
  </article>
  <!-- 16 table -->
  <article class="slide">
    <div class="h" style="left:14px;top:14px">OUR PLANS</div>
    <div class="p" style="left:14px;top:40px;width:110px">Choose the plan that fits your stage of growth.</div>
    <table style="left:140px;top:30px;width:186px">
      <tr><th>Plan</th><th>Start</th><th>Grow</th><th>Scale</th></tr>
      <tr><td>Coaching</td><td>2h</td><td>6h</td><td>12h</td></tr>
      <tr><td>Strategy</td><td>Yes</td><td>Yes</td><td>Yes</td></tr>
      <tr><td>Funding</td><td>No</td><td>Yes</td><td>Yes</td></tr>
      <tr><td>Network</td><td>No</td><td>No</td><td>Yes</td></tr>
      <tr><td>Price</td><td>$99</td><td>$299</td><td>$599</td></tr>
    </table>
  </article>
  <!-- 17 donut -->
  <article class="slide">
    <div class="h" style="left:14px;top:14px">NUMBERS</div>
    <div class="p" style="left:14px;top:40px;width:110px">Share of clients by sector this year.</div>
    <svg style="left:170px;top:25px" width="130" height="130" viewBox="0 0 42 42">
      <circle cx="21" cy="21" r="15.9" fill="none" stroke="#ffffff" stroke-width="7"/>
      <circle cx="21" cy="21" r="15.9" fill="none" stroke="#1d2857" stroke-width="7" stroke-dasharray="55 45" stroke-dashoffset="25"/>
      <circle cx="21" cy="21" r="15.9" fill="none" stroke="#3b3a8f" stroke-width="7" stroke-dasharray="25 75" stroke-dashoffset="70"/>
    </svg>
  </article>
  <!-- 18 bars -->
  <article class="slide">
    <div class="h" style="left:14px;top:14px">NUMBERS</div>
    <div class="p" style="left:14px;top:40px;width:100px">Yearly growth of our client base.</div>
    <svg style="left:140px;top:30px" width="186" height="130" viewBox="0 0 186 130">
      <line x1="0" y1="128" x2="186" y2="128" stroke="#1d2857" stroke-width="1"/>
      <rect x="8" y="70" width="10" height="58" fill="#3b3a8f"/><rect x="20" y="90" width="10" height="38" fill="#1d2857"/>
      <rect x="52" y="50" width="10" height="78" fill="#3b3a8f"/><rect x="64" y="80" width="10" height="48" fill="#1d2857"/>
      <rect x="96" y="30" width="10" height="98" fill="#3b3a8f"/><rect x="108" y="60" width="10" height="68" fill="#1d2857"/>
      <rect x="140" y="10" width="10" height="118" fill="#3b3a8f"/><rect x="152" y="40" width="10" height="88" fill="#1d2857"/>
    </svg>
  </article>
</section>

</body>
</html>
```